Rack Card for Charter Sail Boat business in SF Bay

We are in need of a rack card design to highlight the business to tourists and locals. 2 sided card 3.86" x 8.39" (full bleed)

We are looking for visually appleaing designs on the front and back but a little more detail on the back.

Use the info provided (text and info) on the website to include the 3 key services (Quick, 1/2 day, fullday) and aspects of the boat, location and other key info for customers (not prices). DO NOT INCLUDE ALL THIS TEXT please pick the elements you would like to fit your design and inform the customer as you would like about the business.

I can also provide photos directly from the video if you think those would fit your design. If video doesn't work on this upload you can view it at the website or facebook page (www.fb.com/tidewrenllc)

Now included a few video pictures in files for your use

Target Market(s)

Tourists and locals to san francisco east bay. 25 - 55 years old. Men and women.

Industry/Entity Type

Entertainment

Colors
0455a3
ec1f27
f3f1f8

Requirements
Must have
• Highlight services, key contact information (email, phone, website site), Visual impact
• 2-sided card - 3.86" x 8.39" (98 x 213 mm)
Nice to have
• facebook link, electric engine(green),

```html
<!DOCTYPE html>
<html lang="en">
<head>
<meta charset="utf-8">
<title>Tidewren Rack Card</title>
<link rel="stylesheet" href="https://fonts.googleapis.com/css2?family=PT+Sans+Narrow:wght@400;700&family=Cormorant+Garamond:ital,wght@1,600&family=Questrial&family=Roboto:wght@900&family=Oswald:wght@600&display=swap">
<style>
:root{
  --blue:#0455a3;
  --blue-light:#2a86d6;
  --red:#ec1f27;
  --red-dark:#c8161d;
  --paper:#ffffff;
  --ink:#2b2b2b;
  --bar:#1d1d1d;
  --bg:#ffffff;
}
*{margin:0;padding:0;box-sizing:border-box}
html,body{width:1200px;height:1200px;overflow:hidden;background:var(--bg)}
.card{position:absolute;top:50px;width:508px;height:1104px;background:var(--paper);overflow:hidden;box-shadow:4px 6px 10px rgba(0,0,0,.35)}
.card--front{left:78px}
.card--back{left:644px}
.card__art{position:absolute;left:0;top:0;width:508px;height:1104px}
.brand{position:absolute;display:flex;align-items:center;gap:10px;font-family:"PT Sans Narrow",sans-serif;font-weight:700}
.brand__dot{width:16px;height:16px;border-radius:50%}
.brand--top{left:0;right:0;top:68px;justify-content:center;font-size:58px;color:var(--blue)}
.brand--top .brand__dot{background:var(--red)}
.brand--foot{left:26px;top:968px;font-size:46px;color:#fff}
.brand--foot .brand__dot{background:#fff}
.hero-title{position:absolute;right:42px;top:428px;text-align:right;line-height:1}
.hero-title__lead{font-family:"Questrial",sans-serif;font-size:44px;color:#fff;display:block}
.hero-title__place{font-family:"Roboto",sans-serif;font-weight:900;font-size:46px;color:var(--red);display:block;margin-top:2px}
.hero-title__kind{font-family:"Cormorant Garamond",serif;font-style:italic;font-weight:600;font-size:43px;color:#fff;display:block;margin-top:6px}
.copy{position:absolute;font-family:"PT Sans Narrow",sans-serif;font-size:12.6px;line-height:17.6px;color:var(--ink);text-align:justify}
.copy p{margin-bottom:5px}
.copy--intro{left:42px;right:42px;top:592px}
.copy--modern{left:48px;right:36px;top:876px;color:#fff}
.heading{font-family:"Cormorant Garamond",serif;font-style:italic;font-weight:600;font-size:25px;line-height:26px;color:var(--red);margin-bottom:2px}
.copy--modern .heading{color:#fff}
.copy--details{left:38px;right:38px;top:374px}
.copy--details .heading{margin-top:8px}
.copy--details .heading:first-child{margin-top:0}
.cta{position:absolute;left:0;right:0;top:1040px;text-align:center;font-family:"Oswald",sans-serif;font-weight:600;font-size:31px;line-height:1;color:#fff}
.site-bar{position:absolute;left:0;right:0;bottom:0;height:30px;background:var(--bar);color:#fff;font-family:"Questrial",sans-serif;font-size:17px;letter-spacing:12px;text-align:center;line-height:30px;padding-left:12px}
.contact{position:absolute;right:20px;top:964px;font-family:"PT Sans Narrow",sans-serif;font-size:14px;color:#fff;text-align:right;list-style:none}
.contact li{display:flex;justify-content:flex-end;align-items:center;gap:6px;height:31px}
.contact svg{width:13px;height:14px}
</style>
</head>
<body>

<section class="card card--front">
  <svg class="card__art" viewBox="0 0 508 1104">
    <defs>
      <linearGradient id="dockPhoto" x1="0" y1="0" x2="1" y2="1">
        <stop offset="0" stop-color="#7fb2e6"/>
        <stop offset=".5" stop-color="#b9c4cc"/>
        <stop offset="1" stop-color="#1f2d4a"/>
      </linearGradient>
      <linearGradient id="swoosh" x1="0" y1="0" x2="1" y2="1">
        <stop offset="0" stop-color="var(--blue-light)"/>
        <stop offset="1" stop-color="var(--blue)"/>
      </linearGradient>
      <clipPath id="frontClip"><rect x="0" y="0" width="508" height="574"/></clipPath>
    </defs>
    <rect x="0" y="182" width="508" height="392" fill="url(#dockPhoto)" role="img" aria-label="Photo of the sailboat moored at the marina under a blue sky"/>
    <g clip-path="url(#frontClip)">
      <path transform="translate(-12,-10)" d="M508,118 C420,130 375,230 325,335 C290,405 265,455 245,500 C215,540 150,568 80,574 L508,590 L508,118 Z" fill="var(--red)"/>
      <path transform="translate(-6,-5)" d="M508,118 C420,130 375,230 325,335 C290,405 265,455 245,500 C215,540 150,568 80,574 L508,590 L508,118 Z" fill="#fff"/>
      <path d="M508,118 C420,130 375,230 325,335 C290,405 265,455 245,500 C215,540 150,568 80,574 L508,590 L508,118 Z" fill="url(#swoosh)"/>
    </g>
    <path d="M0,812 C150,892 350,892 508,820 L508,1104 L0,1104 Z" fill="var(--blue)"/>
    <path d="M0,818 C150,900 350,900 508,830 L508,1104 L0,1104 Z" fill="#fff"/>
    <path d="M0,830 C150,910 350,910 508,840 L508,1104 L0,1104 Z" fill="var(--red)"/>
  </svg>

  <div class="brand brand--top"><span class="brand__dot"></span>Tidewren</div>

  <h1 class="hero-title">
    <span class="hero-title__lead">Ultimate</span>
    <span class="hero-title__place">East Bay</span>
    <span class="hero-title__kind">Sailboat Charter</span>
  </h1>

  <div class="copy copy--intro">
    <p>Come enjoy an amazing experience aboard Tidewren and view San Francisco and the rest of the bay as so few are able to do. Tidewren is a supreme blue-water cruising boat with all the modern safety, comfort and entertainment equipment you would expect. Your time aboard Tidewren is yours to enjoy and direct as you wish while we show you San Francisco Bay, the Golden Gate Bridge, Alcatraz, Treasure and Angel Islands and so much more.</p>
    <p>Tidewren is located at the Berkeley Marina and perfectly placed to take advantage of the vast and beautiful Bay. Those that live or visit the East Bay or the Central Valley can easily reach the marina and parking is no problem. Within a few minutes of arriving on the boat you can be "shooting the slot" and experiencing the thrill of dropping the rail into the water or warming yourself with refreshment in the protection of Angel Island.</p>
    <p>Come join us and share the wonders around San Francisco Bay with your friends and family. We love to show families how to sail and have great fun on the water while staying safe</p>
  </div>

  <div class="copy copy--modern">
    <h2 class="heading">Modern:</h2>
    <p>Tidewren has undergone a complete overhaul with many upgrades and improvements. She has gone completely electric which means no diesel smells, noise or vibration to suffer. New electrics, plumbing, toilets, and deck areas compliment the elegant lines and features of this Halvard 46 foot cutter rigged sailboat. Everything was inspected and repaired, over-hauled or replaced during the 2 year refit so that you can relax and enjoy the spectacular scenery and natures' wonders without a care. The head (toilet) is almost just like the one you may find in your own home. Just electric and uses much less water!</p>
  </div>

  <p class="cta">CALL TODAY +1 510-555-0148</p>
  <div class="site-bar">tidewren.com</div>
</section>

<section class="card card--back">
  <svg class="card__art" viewBox="0 0 508 1104">
    <defs>
      <linearGradient id="cockpitPhoto" x1="0" y1="0" x2="1" y2="1">
        <stop offset="0" stop-color="#8fc0ee"/>
        <stop offset=".55" stop-color="#5d6f86"/>
        <stop offset="1" stop-color="#2a3550"/>
      </linearGradient>
      <linearGradient id="bayPhoto" x1="0" y1="0" x2="1" y2="1">
        <stop offset="0" stop-color="#e0343a"/>
        <stop offset="1" stop-color="var(--red-dark)"/>
      </linearGradient>
    </defs>
    <rect x="0" y="0" width="508" height="400" fill="url(#cockpitPhoto)" role="img" aria-label="Photo of two children in life jackets in the boat's cockpit"/>
    <path d="M0,312 C130,372 330,378 508,300 L508,420 L0,420 Z" fill="var(--blue)"/>
    <path d="M0,318 C130,378 330,384 508,306 L508,420 L0,420 Z" fill="var(--red)"/>
    <path d="M0,334 C130,394 330,398 508,324 L508,420 L0,420 Z" fill="#fff"/>
    <path d="M150,930 C290,915 420,874 508,836 L508,1104 L0,1104 Z" fill="var(--blue)"/>
    <path d="M160,938 C300,922 424,884 508,846 L508,1104 L0,1104 Z" fill="#fff"/>
    <path d="M168,944 C306,928 428,892 508,854 L508,1104 L0,1104 Z" fill="url(#bayPhoto)" role="img" aria-label="Red-tinted photo of the bay"/>
    <path d="M0,866 C160,874 262,940 282,1104 L0,1104 Z" fill="#fff"/>
    <path d="M0,872 C150,880 252,944 270,1104 L0,1104 Z" fill="var(--blue)"/>
  </svg>

  <div class="copy copy--details">
    <h2 class="heading">The trip</h2>
    <p>When chartering Tidewren, the vessel is yours to direct anywhere within the time you wish to enjoy her. We do have a few old favorites that are always fun that we have listed below. These are just to provide an idea of the possible cruise as every trip takes into account your ideas and natures (tides, weather and currents) will. If your looking for something a little different or to mix it up a bit, let us know and we can make it happen. Our custom trips are simple to arrange and book, we simply ask for a minimum of 3 hours duration</p>
    <h2 class="heading">2 hour Blast</h2>
    <p>Could be a sunset sail, an early morning wake up cruise or a blast out into the bay anytime to find peace, fresh air and amazing views</p>
    <h2 class="heading">½ day Fun</h2>
    <p>A full morning, afternoon or evening out in the Bay seeing many of the main features and landmarks close to the Bay from the water. Actual duration 4-5 hours</p>
    <h2 class="heading">Full Day Adventure</h2>
    <p>The day includes a complete circuit of the Bay and lunch at anchor. Actual duration 7-8 hours</p>
    <h2 class="heading">Tidewren</h2>
    <p>Tidewren is a 50 foot, center cockpit, cutter rigged, mono-hulled, blue water cruising sail boat. What does that mean to you and me... she's a nice sized boat with the driving position and main seats at the center of the boat. She has three positions for sails, main (the big one), jib (front sail) and stay-sail (between main and jib). She has a single hull so will lean over as the wind blows. This is important as this safely removes pressure and force from the rig in heavy weather. The blue water bit just means she was designed to race and cruise long distance and in open oceans</p>
  </div>

  <div class="brand brand--foot"><span class="brand__dot"></span>Tidewren</div>

  <ul class="contact">
    <li>48 Harbor Point Rd Berkeley, CA 94710
      <svg viewBox="0 0 12 14"><path d="M6 0a4.5 4.5 0 0 0-4.5 4.5C1.5 8 6 14 6 14s4.5-6 4.5-9.5A4.5 4.5 0 0 0 6 0zm0 6.3a1.8 1.8 0 1 1 0-3.6 1.8 1.8 0 0 1 0 3.6z" fill="var(--blue-light)"/></svg></li>
    <li>+1 510-555-0148
      <svg viewBox="0 0 14 14"><path d="M3 1l2.2 2.6-1.3 1.6c.8 1.8 2.2 3.2 4 4l1.6-1.3L12 10l-1.2 2.4C6 12.2 1.8 8 1.6 3.2z" fill="var(--blue-light)"/></svg></li>
    <li>www.fb.com/tidewrenllc
      <svg viewBox="0 0 14 14"><circle cx="7" cy="7" r="6" fill="var(--blue-light)"/></svg></li>
  </ul>

  <div class="site-bar">tidewren.com</div>
</section>

</body>
</html>
```